Business Card Design

I am starting my therapy private practice. I will be an in home therapist, so I go into family's homes instead of using an office to do family/marriage therapy. Therefore, I do not have an office address. I am looking for something in the black, red, gray, and blue color scheme that appeals to both families, couples and teenagers.

Industry/Entity Type

Business

Contact Information for Business Card

Lena Brightwell, MS, MFT Intern
Marriage and Family Therapy
In Home Therapist
617-482-5190
Lena@LenaBrightwell-example.com

```html
<!DOCTYPE html>
<html lang="en">
<head>
<meta charset="utf-8">
<title>Lena Brightwell – Business Card</title>
<link rel="stylesheet" href="https://fonts.googleapis.com/css2?family=Open+Sans:wght@300;400;700&display=swap">
<style>
  :root {
    --backdrop: #e8e5e0;
    --paper: #ffffff;
    --red: #c8203a;
    --red-deep: #a8152c;
    --red-light: #d83a52;
    --blue: #2a7fc4;
    --ink: #4a4a4a;
    --ink-soft: #8c8c8c;
    --white: #ffffff;
  }
  * { box-sizing: border-box; margin: 0; padding: 0; }
  html, body {
    width: 1200px; height: 1023px; overflow: hidden;
    background: var(--backdrop);
    font-family: "Open Sans", Arial, sans-serif;
  }
  .card {
    position: absolute; left: 200px;
    width: 800px; height: 457px;
    overflow: hidden;
    box-shadow: 0 6px 18px rgba(0,0,0,0.15);
  }
  .card-front { top: 40px; background: var(--paper); }
  .card-back {
    top: 526px;
    background: linear-gradient(135deg, var(--red-deep) 0%, var(--red) 55%, var(--red-light) 100%);
    display: flex; align-items: center; justify-content: center;
  }

  /* brand lockup */
  .brand { display: flex; align-items: center; gap: 18px; }
  .brand-mark { width: 26px; height: 26px; }
  .brand-name { font-weight: 300; letter-spacing: 0.5px; }
  .card-front .brand { position: absolute; left: 64px; top: 92px; }
  .card-front .brand-mark { background: var(--blue); }
  .card-front .brand-name { font-size: 44px; color: var(--ink-soft); }
  .card-back .brand-mark { background: var(--white); width: 30px; height: 30px; }
  .card-back .brand-name { font-size: 50px; color: var(--white); }

  /* identity */
  .therapist-name {
    position: absolute; left: 64px; top: 214px;
    font-size: 34px; font-weight: 700; color: var(--ink);
  }
  .therapist-role {
    position: absolute; left: 64px; top: 264px;
    font-size: 20px; font-weight: 400; color: var(--ink);
  }

  /* contact band */
  .contact-band {
    position: absolute; left: 0; right: 0; top: 316px; bottom: 0;
    background: linear-gradient(180deg, var(--red-light), var(--red));
    border-top: 5px solid var(--blue);
    padding: 26px 64px 0;
  }
  .contact-line {
    display: flex; align-items: center; gap: 14px;
    color: var(--white); font-size: 20px; font-weight: 400;
    margin-bottom: 14px;
  }
  .contact-icon { width: 18px; height: 18px; flex: none; }
  .band-heart {
    position: absolute; right: 40px; top: 258px;
    width: 92px; height: 72px;
  }
</style>
</head>
<body>

<section class="card card-front">
  <div class="brand">
    <span class="brand-mark"></span>
    <span class="brand-name">Hearthside Therapy</span>
  </div>

  <h1 class="therapist-name">Lena Brightwell MS, MFT</h1>
  <p class="therapist-role">Intern Marriage and Family Therapy In Home Therapist</p>

  <svg class="band-heart" viewBox="0 0 92 72" aria-hidden="true">
    <path d="M46 70 C20 52 4 38 4 22 C4 10 14 2 25 2 C35 2 42 8 46 16 C50 8 57 2 67 2 C78 2 88 10 88 22 C88 38 72 52 46 70 Z" fill="var(--red)"/>
  </svg>

  <div class="contact-band">
    <p class="contact-line">
      <svg class="contact-icon" viewBox="0 0 24 24" aria-hidden="true">
        <path d="M6.6 10.8a15 15 0 0 0 6.6 6.6l2.2-2.2a1 1 0 0 1 1-.25 11.4 11.4 0 0 0 3.6.57 1 1 0 0 1 1 1V20a1 1 0 0 1-1 1A17 17 0 0 1 3 4a1 1 0 0 1 1-1h3.5a1 1 0 0 1 1 1c0 1.25.2 2.45.57 3.57a1 1 0 0 1-.25 1z" fill="var(--white)"/>
      </svg>
      617-482-5190
    </p>
    <p class="contact-line">
      <svg class="contact-icon" viewBox="0 0 24 24" aria-hidden="true">
        <rect x="2" y="5" width="20" height="14" rx="1.5" fill="none" stroke="var(--white)" stroke-width="2"/>
        <path d="M3 6l9 7 9-7" fill="none" stroke="var(--white)" stroke-width="2"/>
      </svg>
      Lena@LenaBrightwell-example.com
    </p>
  </div>
</section>

<section class="card card-back">
  <div class="brand">
    <span class="brand-mark"></span>
    <span class="brand-name">Hearthside Therapy</span>
  </div>
</section>

</body>
</html>
```